Business Cards

We are wanting business cards created using previous design #36167008 as a starting point.
Info needed on front side:
Employee Name
Title
Email
Phone Number

Info needed on back side: (these are our product lines)
Frac Valves Fishing
Flowback Thru-Tubing
Torque & Test LMQV

please see changes

```html
<!DOCTYPE html>
<html lang="en">
<head>
<meta charset="utf-8">
<title>Business Cards – Talon Downhole LLC &amp; Summit Yield Services</title>
<link rel="stylesheet" href="https://fonts.googleapis.com/css2?family=Cinzel:wght@400;600&family=Montserrat:wght@300;500;700&display=swap">
<style>
  :root {
    --backdrop: #9c9c9c;
    --card: #1b1b1b;
    --tan: #e2c595;
    --bronze: #a8916f;
    --white: #ffffff;
    --ink: #1b1b1b;
    --muted: #e9e9e9;
  }
  * { box-sizing: border-box; margin: 0; padding: 0; }
  html, body {
    width: 1200px; height: 1200px; overflow: hidden;
    background: var(--backdrop);
  }
  .card {
    position: absolute; left: 217px; width: 786px; height: 472px;
    background: var(--card);
  }
  .card--front { top: 116px; }
  .card--back { top: 646px; }

  .holder-name {
    position: absolute; left: 41px; top: 56px;
    font-family: "Cinzel", serif; font-weight: 400;
    font-size: 36px; color: var(--tan); letter-spacing: 0.5px;
  }
  .holder-title {
    position: absolute; left: 39px; top: 100px;
    font-family: "Montserrat", sans-serif; font-weight: 500;
    font-size: 20px; color: var(--white);
  }
  .address {
    position: absolute; left: 39px; top: 245px;
    font-family: "Montserrat", sans-serif; font-weight: 300; font-style: normal;
    font-size: 18px; line-height: 25.5px; color: var(--muted);
  }
  .contacts {
    position: absolute; left: 38px; top: 355px; list-style: none;
    font-family: "Montserrat", sans-serif; font-weight: 300;
    font-size: 18px; color: var(--muted);
  }
  .contacts li { display: flex; align-items: center; height: 25.5px; }
  .contacts svg { width: 15px; height: 15px; margin-right: 10px; flex: none; }
  .contacts .accent { color: var(--tan); font-weight: 500; }

  .brand {
    position: absolute; width: 200px; display: flex; align-items: center; gap: 10px;
    font-family: "Montserrat", sans-serif; font-weight: 700;
    color: var(--tan); text-transform: uppercase; line-height: 1.2;
    transform: translateY(-50%);
  }
  .brand__mark { flex: none; }
  .brand__mark--circle {
    width: 32px; height: 32px; border-radius: 50%;
    border: 4px solid var(--bronze);
  }
  .brand__mark--square {
    width: 30px; height: 30px; border: 4px solid var(--bronze);
  }
  .brand__name { font-size: 17px; letter-spacing: 0.5px; white-space: nowrap; }

  .card--front .brand--summit { left: 518px; top: 135px; }
  .card--front .brand--talon { left: 518px; top: 340px; }
  .card--back .brand--talon { left: 190px; top: 200px; }
  .card--back .brand--summit { left: 410px; top: 200px; }

  .product-lines {
    position: absolute; left: 69px; top: 314px; width: 648px; height: 28px;
    background: var(--tan); border-radius: 5px;
    display: flex; align-items: center; justify-content: center; gap: 7px;
    font-family: "Cinzel", serif; font-weight: 600; font-size: 13.5px;
    text-transform: uppercase; color: var(--ink); white-space: nowrap;
  }
  .product-lines .dot {
    width: 7px; height: 7px; border-radius: 50%; background: var(--ink); flex: none;
  }
</style>
</head>
<body>
  <section class="card card--front">
    <h1 class="holder-name">Corin Halvorsen</h1>
    <p class="holder-title">Director</p>

    <address class="address">
      12 Larkfield Row 3rd Floor<br>
      Ashbury AB1 4QX,<br>
      United Kingdom
    </address>

    <ul class="contacts">
      <li>
        <svg viewBox="0 0 16 16" aria-hidden="true"><path d="M4 1.5l2.2 2.6-1.2 1.6c.9 2 2.3 3.4 4.3 4.3l1.6-1.2 2.6 2.2-1.4 2.3C7 13 3 9 1.7 3.1z" fill="none" stroke="#e2c595" stroke-width="1.4" stroke-linejoin="round"/></svg>
        +1 555 014 3827
      </li>
      <li>
        <svg viewBox="0 0 16 16" aria-hidden="true"><rect x="1" y="4" width="14" height="10" fill="none" stroke="#e2c595" stroke-width="1.4"/><path d="M1 4l7 5 7-5" fill="none" stroke="#e2c595" stroke-width="1.4"/></svg>
        hello@northmarkwell.com
      </li>
      <li>
        <svg viewBox="0 0 16 16" aria-hidden="true"><circle cx="8" cy="8" r="6.5" fill="none" stroke="#e2c595" stroke-width="1.2"/><ellipse cx="8" cy="8" rx="3" ry="6.5" fill="none" stroke="#e2c595" stroke-width="1.2"/><path d="M1.5 8h13M2.5 5h11M2.5 11h11" stroke="#e2c595" stroke-width="1.1"/></svg>
        <span>www.<span class="accent">northmarkwell</span>.com</span>
      </li>
    </ul>

    <div class="brand brand--summit">
      <span class="brand__mark brand__mark--square"></span>
      <span class="brand__name">Summit Yield<br>Services</span>
    </div>
    <div class="brand brand--talon">
      <span class="brand__mark brand__mark--circle"></span>
      <span class="brand__name">Talon<br>Downhole LLC</span>
    </div>
  </section>

  <section class="card card--back">
    <div class="brand brand--talon">
      <span class="brand__mark brand__mark--circle"></span>
      <span class="brand__name">Talon<br>Downhole LLC</span>
    </div>
    <div class="brand brand--summit">
      <span class="brand__mark brand__mark--square"></span>
      <span class="brand__name">Summit Yield<br>Services</span>
    </div>

    <p class="product-lines">
      <span>Frac Valves Fishing</span><span class="dot"></span>
      <span>Flowback Thru-Tubing</span><span class="dot"></span>
      <span>Torque &amp; Test LMQV</span>
    </p>
  </section>
</body>
</html>
```